Contractor Business Card Design

Looking to have a card made that has a bold description of (KITCHENS, BASEMENTS, BATHROOMS)

Definition and layers a plus

Contact info is;

Mark T. Ellery
Millbrook, MN 55410
Cell: 612-555-0147
website: www.cobaltfinishworks.example
Email: cobaltfinishworksmn@mailbox.example

colors: red, black, gray, white

Contact Information for Business Card

Contact info is;

Mark T. Ellery
Millbrook, MN 55410
Cell: 612-555-0147

Colors
ec1f27

Requirements
Must have
• Looking for layers and definition
Nice to have
• Cards are planned to be printed on plastic cards

```html
<!DOCTYPE html>
<html lang="en">
<head>
<meta charset="utf-8">
<title>Cobalt Finishworks – Business Card</title>
<link rel="stylesheet" href="https://fonts.googleapis.com/css2?family=Source+Sans+3:wght@400;700&display=swap">
<style>
  :root {
    --brand-red: #ec1f27;
    --name-red: #e0195a;
    --charcoal: #2b2e30;
    --charcoal-deep: #1f2123;
    --card-light: #ececec;
    --card-light-deep: #dcdcdc;
    --ink: #222222;
    --white: #f4f4f4;
    --page: #ffffff;
  }
  * { box-sizing: border-box; margin: 0; padding: 0; }
  html, body {
    width: 1004px; height: 1200px; overflow: hidden;
    background: var(--page);
    font-family: "Source Sans 3", sans-serif;
  }
  .card {
    position: absolute; left: 210px; width: 584px; height: 325px;
    overflow: hidden;
  }
  .card--front { top: 255px; }
  .card--back { top: 619px; border: 1px solid #c9c9c9; }
  .card__texture { position: absolute; inset: 0; }
  .card--front .card__texture {
    background: radial-gradient(ellipse at 50% 45%, var(--charcoal) 0%, var(--charcoal-deep) 100%);
  }
  .card--back .card__texture {
    background: radial-gradient(ellipse at 50% 45%, var(--card-light) 0%, var(--card-light-deep) 100%);
  }
  .brand-mark { position: absolute; }
  .card--front .brand-mark { left: 245px; top: 56px; }
  .card--back .brand-mark { left: 96px; top: 47px; }
  .brand-name {
    position: absolute; width: 240px; text-align: center;
    font-weight: 700; font-size: 23px; line-height: 1.15;
    letter-spacing: 2px; text-transform: uppercase; white-space: nowrap;
  }
  .card--front .brand-name { left: 172px; top: 160px; color: var(--white); }
  .card--back .brand-name { left: 30px; top: 172px; color: var(--ink); }
  .services {
    position: absolute; left: 0; right: 0; top: 276px;
    text-align: center; font-size: 18px; color: var(--white);
    white-space: nowrap;
  }
  .services__accent { color: var(--brand-red); }
  .services__divider { margin: 0 3px; }
  .person-name {
    position: absolute; left: 329px; top: 34px;
    font-size: 26px; font-weight: 400; color: var(--name-red);
    white-space: nowrap;
  }
  .contact {
    position: absolute; left: 329px; top: 196px;
    list-style: none; font-size: 12.5px; line-height: 19.3px; color: var(--ink);
    white-space: nowrap;
  }
</style>
</head>
<body>
  <section class="card card--front">
    <div class="card__texture" role="img" aria-label="Dark quilted diamond texture background"></div>
    <svg class="brand-mark" width="94" height="94" viewBox="0 0 94 94" aria-hidden="true">
      <circle cx="47" cy="47" r="44" fill="none" stroke="var(--white)" stroke-width="3"/>
    </svg>
    <div class="brand-name">Cobalt<br>Finishworks</div>
    <p class="services">
      <span class="services__accent">KITCHENS</span><span class="services__divider">|</span>BASEMENTS<span class="services__divider">|</span><span class="services__accent">BATHROOMS</span>
    </p>
  </section>

  <section class="card card--back">
    <div class="card__texture" role="img" aria-label="Light quilted diamond texture background"></div>
    <svg class="brand-mark" width="108" height="108" viewBox="0 0 108 108" aria-hidden="true">
      <circle cx="54" cy="54" r="51" fill="none" stroke="var(--ink)" stroke-width="3"/>
    </svg>
    <div class="brand-name">Cobalt<br>Finishworks</div>
    <h1 class="person-name">Mark T. Ellery</h1>
    <ul class="contact">
      <li>Millbrook, MN 55410</li>
      <li>Cell: 612-555-0147</li>
      <li>website: www.cobaltfinishworks.example</li>
      <li>Email: cobaltfinishworksmn@mailbox.example</li>
    </ul>
  </section>
</body>
</html>
```